Marlowick community hall home page

We are building a modern, responsive website & booking system for our community hall. For this PixelForge task, we would like to receive design ideas for the home page.
There are no limits on the colours or fonts that can be used. We are looking for a modern, fresh design with a local/community feel. We don’t have a logo but we also recognise that our name is quite long! … So initials (MCH) instead of the name would be fine.
People book our community hall for a range of activities including: fitness classes, wedding receptions, birthday parties, business meetings, teaching, community events, charity fundraisers and other celebrations.
We have three main goals for the website. The first is that people can check our calendar and make a booking for an available time slot. The second is that they can read about our facilities and the prices for hiring them. The third is that people can find out about upcoming activities & events.
CTA: Book now
A button that links to a booking request form. (The form is not part of this design project)
Primary/Header navigation:
Home | Calendar | Facilities | Prices | Photos | News | Contact
Secondary/Footer navigation:
Chatterleaf | Quillcast
Login | Register | Privacy policy | Terms & conditions
Example texts (lorem ipsum etc. is also fine):
We have everything you need from a venue, whether it’s an elegant room with ample flexible space, a lavish and elegant hall for a wedding reception, a conference room that fits 125 delegates or a easy access venue to the town centre.
The hall is available for hire for wedding receptions, birthday celebrations, anniversaries, children's parties, presentations, lectures, fitness groups, and will comfortably accommodate all your guests.
This venue is well equipped with a modern kitchen, a range of audio and technical services, hearing loop, licensed bar, conference facilities, disabled access and unlimited free WiFi.
You can use this website to find out more about our rooms, equipment and the services we can offer and use the calendar to see where we have rooms available. You can also book rooms using our online booking system.
To the front of the building is a large public open grassed area across which is a row of shops. To the rear of the building is the large car park, including spaces for blue badge holders and a large enclosed cycle rack. This area also has extensive gardens, with seating and planting areas maintained by local volunteers.
The community hall is run and managed by volunteers of the Marlowick Community Organisation. Our objectives are to increase opportunities for people living in and around Marlowick.
We are passionate about being the heart of the community; caring for this community centred property and visitors are at the heart of all we do.
Where to go next
— Check when the hall is free
— Read our booking policy documents
— Make a booking reservation
Amenities
— Free WiFi
— Free car parking
— Fully equipped kitchen
— Hearing loop
Details for our most popular facilities (rooms):
Name: Main hall
Short description: A 127 square metre main hall with entrance lobby, toilets, a well-equipped kitchen and separate storage facilities. Three sets of double doors provide access to a large paved area and the adjacent playing field.
Capacity: 180 people
Price: £10-20 per hour
Links: More info | Book now
Name: Large meeting room
Short description: A delightful, spacious room with an outlook and access to the small walled garden. Ideal for meetings and small gatherings - it has its own access door and the use of a disabled W/C. We offer a reduced rate for this room when booked together with the main hall.
Capacity: 20 people
Price: £6-12 per hour
Attachments:
We have attached some photos of the hall & some (royalty free) stock images for inspiration.

```html
<!DOCTYPE html>
<html lang="en">
<head>
<meta charset="utf-8">
<title>Marlowick Community Hall</title>
<link href="https://fonts.googleapis.com/css2?family=Raleway:wght@500;600;700&family=Roboto:wght@400;500;700&display=swap" rel="stylesheet">
<style>
:root{
  --orange:#ee5a24;
  --orange-soft:#f26b3a;
  --ink:#111;
  --text:#666;
  --dark:#141414;
  --grey-line:#ddd;
  --white:#fff;
}
*{box-sizing:border-box;margin:0;padding:0}
html,body{width:1200px;height:4688px;overflow:hidden;background:#fff}
body{position:relative;font-family:"Roboto",Arial,sans-serif;color:var(--ink)}
.abs{position:absolute}
h1,h2,h3,h4{font-family:"Raleway",Arial,sans-serif}

/* hero */
.hero{left:0;top:0;width:1200px;height:686px;background:linear-gradient(160deg,#4a2f6e 0%,#2b1f3a 35%,#241c26 60%,#3b2a38 100%)}
.hero::after{content:"";position:absolute;inset:0;background:rgba(10,8,20,.35)}
.logo{left:109px;top:38px;z-index:2;color:#fff;font:700 27px "Raleway",sans-serif;letter-spacing:1px}
.nav{left:479px;top:52px;z-index:2;display:flex;gap:0;font:600 12.5px "Raleway",sans-serif;color:#fff}
.nav a{position:absolute;white-space:nowrap;color:#fff;text-decoration:none}
.nav a.active{color:var(--orange)}
.hero-title{left:0;width:1200px;top:308px;z-index:2;text-align:center;color:#fff;font:600 42px "Raleway",sans-serif;letter-spacing:.5px}
.btn{display:inline-block;border-radius:24px;text-align:center;font:600 13px "Raleway",sans-serif;text-transform:uppercase}
.hero-cta{left:516px;top:386px;width:168px;height:46px;line-height:46px;background:var(--orange);color:#fff;z-index:2}
.notch{left:540px;top:646px;z-index:3}

/* features */
.feature{top:732px;display:flex;align-items:center;gap:18px;font-size:15px;color:#777;line-height:22px}

/* section headings */
.sec-title{left:0;width:1200px;text-align:center;font:700 37px "Raleway",sans-serif;color:#111;text-transform:uppercase}
.divider{left:460px;width:280px;height:16px}
.lead{left:185px;width:830px;text-align:center;font-size:13px;line-height:22.5px;color:#777}
.photo{top:1080px;width:237px;height:231px}

/* facilities */
.fac{top:1500px;width:600px;height:532px;padding:86px 0 0 111px;color:#fff}
.fac-left{left:0;background:linear-gradient(135deg,#2a2622,#1a1816 60%,#2d2824)}
.fac-right{left:600px;background:linear-gradient(135deg,#ef6a36,#f07a48);padding-left:92px}
.fac h3{font-size:25px;font-weight:600;margin-bottom:20px}
.fac p{font-size:13px;line-height:22px;width:420px}
.fac .label{font:600 13px "Raleway",sans-serif;margin-top:28px}
.fac .value{font:600 21px "Raleway",sans-serif;margin-top:10px}
.fac .btns{display:flex;gap:6px;margin-top:28px}
.fac .btn{width:170px;height:46px;line-height:46px;font-size:12px}
.b-white{background:#fff;color:#111}
.b-orange{background:var(--orange);color:#fff}
.b-black{background:#000;color:#fff}

/* calendar */
.calendar{left:104px;top:2225px;width:506px;height:312px;border:1px solid #e6e6e6;box-shadow:0 2px 8px rgba(0,0,0,.06);padding:20px 24px}
.cal-month{font:600 44px "Raleway",sans-serif;color:#a8a8a8}
.cal-year{position:absolute;right:26px;top:44px;color:var(--orange);font:700 18px "Raleway",sans-serif}
.cal-grid{position:absolute;left:24px;top:82px;display:grid;grid-template-columns:repeat(7,65px);gap:3px 1px}
.cal-grid span{height:30px;font-size:11px;color:#555;display:flex;align-items:flex-end;justify-content:flex-end;padding:0 5px 3px 0;border-bottom:1px solid #e8e8e8}
.cal-grid .hd{height:16px;background:#bbb;color:#fff;justify-content:center;align-items:center;padding:0;font-weight:500;border:0}
.cal-grid .hd.sun{background:#d84f45}
.cal-grid .sunc{background:#eee}
.cal-grid .mark{background:var(--orange);color:#fff}
.free-title{left:652px;top:2262px;font:600 20px "Raleway",sans-serif}
.days{left:652px;top:2302px;display:flex;gap:16px}
.days span{width:46px;height:46px;border-radius:50%;background:#111;color:#fff;display:flex;align-items:center;justify-content:center;font:700 18px "Raleway",sans-serif}
.days span:first-child{background:var(--orange)}
.free-text{left:658px;top:2366px;width:400px;font-size:12.5px;line-height:22px;color:#888}
.policy{left:654px;top:2450px;width:254px;height:44px;line-height:44px;background:var(--orange);color:#fff;font-size:12.5px}

/* amenities */
.amen{left:0;top:2635px;width:1200px;height:333px;background:linear-gradient(90deg,#e8521e,#f0652e 50%,#e8521e)}
.amen-title{top:2684px;color:#fff}
.amen-item{top:2790px;width:240px;text-align:center;color:#fff;font:600 19px "Raleway",sans-serif}
.amen-item .circle{width:94px;height:94px;border-radius:50%;background:#fff;margin:0 auto 18px;display:flex;align-items:center;justify-content:center}

/* events */
.event{top:3165px;width:472px;height:340px}
.event .img{width:472px;height:258px}
.event .date{position:absolute;left:0;top:235px;width:91px;height:105px;background:var(--orange);color:#111;text-align:center;padding-top:18px}
.event .date b{display:block;font:600 19px "Raleway",sans-serif}
.event .date strong{display:block;font:700 34px "Raleway",sans-serif;line-height:40px}
.event h4{position:absolute;left:117px;top:282px;width:330px;font-size:16.5px;font-weight:600;line-height:22px}

/* news */
.news{top:3702px;width:310px;height:395px;border:1px solid #e5e5e5;box-shadow:0 1px 6px rgba(0,0,0,.06);padding:5px}
.news .img{height:194px}
.news h4{margin:24px 0 0 20px;font-size:17px;font-weight:600;line-height:24px;color:#222}
.news .date{margin:16px 0 0 20px;font-size:12.5px;color:#999;display:flex;align-items:center;gap:5px}
.news p{margin:14px 0 0 20px;font-size:12.5px;line-height:24px;color:#999;width:270px}

/* footer */
.footer{left:0;top:4194px;width:1200px;height:494px;background:#000;color:#fff}
.f-title{font:700 23px "Raleway",sans-serif}
.f-sub{font-size:13px;color:#ddd}
.field{width:218px;height:42px;border:1px solid #bbb;color:#fff;font-size:12px;padding:13px 0 0 14px}
.submit{left:120px;top:4489px;width:454px;height:50px;line-height:50px;background:var(--orange);text-align:center;font:700 17px "Roboto",sans-serif}
.contact{left:648px;top:4275px;width:300px}
.c-row{display:flex;gap:14px;font-size:13.5px;line-height:21px;margin-top:16px}
.c-row svg{flex:none;margin-top:2px}
.links{left:950px;top:4275px}
.links ul{list-style:none;margin-top:28px;font-size:14px;line-height:29px;color:#ddd;padding-left:10px}
.bottom{top:4616px;font-size:13px;color:#ddd}
.social{left:546px;top:4608px;display:flex;gap:10px}
.social span{height:38px;padding:0 12px;border-radius:19px;background:#333;line-height:38px;font-size:11px;color:#fff}
</style>
</head>
<body>

<!-- hero -->
<div class="abs hero" role="img" aria-label="Guests seated at round tables in the hall under purple lighting with stained glass windows"></div>
<div class="abs logo">MCH</div>
<nav class="abs nav" style="left:0;top:52px">
  <a class="active" style="left:479px">HOME</a>
  <a style="left:555px">CALENDAR</a>
  <a style="left:665px">FACILITIES</a>
  <a style="left:770px">PRICES</a>
  <a style="left:854px">PHOTOS</a>
  <a style="left:945px">NEWS</a>
  <a style="left:1023px">CONTACT</a>
</nav>
<h1 class="abs hero-title">MARLOWICK COMMUNITY HALL</h1>
<a class="abs btn hero-cta">Get Started</a>
<svg class="abs notch" width="120" height="42" viewBox="0 0 120 42">
  <path d="M0 42 C30 42 38 0 60 0 C82 0 90 42 120 42 Z" fill="#fff"/>
  <rect x="52" y="12" width="16" height="24" rx="8" fill="none" stroke="#555" stroke-width="1.6"/>
  <line x1="60" y1="17" x2="60" y2="22" stroke="#555" stroke-width="1.6"/>
</svg>

<!-- features -->
<div class="abs feature" style="left:44px">
  <svg width="46" height="46" viewBox="0 0 46 46" fill="none" stroke="#555" stroke-width="1.6"><path d="M4 16 L23 5 L42 16 Z"/><line x1="6" y1="19" x2="40" y2="19"/><path d="M10 21v16M18 21v16M28 21v16M36 21v16"/><rect x="4" y="38" width="38" height="4"/></svg>
  <span>The best<br>Community Hall</span>
</div>
<div class="abs feature" style="left:330px">
  <svg width="48" height="48" viewBox="0 0 48 48" fill="none" stroke="#555" stroke-width="1.6"><path d="M40 20 A17 17 0 1 0 24 41"/><path d="M23 12v12l7 5"/><path d="M36 8l4 12-12-2"/><text x="26" y="46" font-size="15" fill="#555" stroke="none" font-family="Roboto">24</text></svg>
  <span>Customer services<br>spanish 24/7</span>
</div>
<div class="abs feature" style="left:644px">
  <svg width="50" height="46" viewBox="0 0 50 46" fill="none" stroke="#555" stroke-width="1.6"><circle cx="25" cy="20" r="12"/><path d="M25 13l2.2 4.5 5 .7-3.6 3.5.8 5-4.4-2.3-4.4 2.3.8-5-3.6-3.5 5-.7z"/><path d="M6 38h38M12 32l-6 6M38 32l6 6"/></svg>
  <span>Thousands of openion<br>from real customer</span>
</div>
<div class="abs feature" style="left:955px">
  <svg width="46" height="48" viewBox="0 0 46 48" fill="none" stroke="#555" stroke-width="1.6"><path d="M14 10h14l-3 6h-8z"/><path d="M16 16C6 22 6 42 12 44h18c6-2 6-22-4-28"/><circle cx="32" cy="34" r="8"/><text x="28" y="38" font-size="11" fill="#555" stroke="none" font-family="Roboto">€</text></svg>
  <span>No surcharges or<br>hidden costs</span>
</div>

<!-- welcome -->
<h2 class="abs sec-title" style="top:864px">Welcome to Marlowick</h2>
<svg class="abs divider" style="top:924px" viewBox="0 0 280 16"><line x1="0" y1="8" x2="280" y2="8" stroke="#333" stroke-width="1"/><rect x="110" y="2" width="60" height="12" rx="6" fill="#fff" stroke="#333"/></svg>
<p class="abs lead" style="top:964px">Lorem ipsum dolor sit amet, consectetur adipiscing elit, sed do eiusmod tempor incididunt ut labore et dolore magna aliqua. Ut enim ad minim veniam, quis nostrud exercitation ullamco laboris nisi ut aliquip ex ea commodo consequat. Duis aute irure dolor in reprehenderit in voluptate velit esse cillum dolore eu fugiat nulla pariatur. Excepteur sint occaecat cupidatat non proident, sunt in culpa qui officia deserunt mollit anim id est laborum.</p>
<div class="abs photo" style="left:111px;background:linear-gradient(160deg,#cfd8d6,#d9a873 60%,#7d6db3)" role="img" aria-label="Meeting room with tables and purple chairs"></div>
<div class="abs photo" style="left:358px;background:linear-gradient(180deg,#e9e7e2,#c9c3b8 55%,#6b5c4c)" role="img" aria-label="Conference layout with projector screen"></div>
<div class="abs photo" style="left:605px;background:linear-gradient(160deg,#6a8fb5,#d9c23a 55%,#a38a24)" role="img" aria-label="Child playing on a bouncy castle"></div>
<div class="abs photo" style="left:852px;background:linear-gradient(150deg,#e8ddd3,#d8b08c 60%,#b47a58)" role="img" aria-label="Icing being piped onto a biscuit"></div>

<!-- facilities -->
<h2 class="abs sec-title" style="top:1396px">Details for our most popular facilities</h2>
<svg class="abs divider" style="top:1456px" viewBox="0 0 280 16"><line x1="0" y1="8" x2="280" y2="8" stroke="#333"/><rect x="110" y="2" width="60" height="12" rx="6" fill="#fff" stroke="#333"/></svg>
<div class="abs fac fac-left" role="img" aria-label="Main hall interior, darkened">
  <h3>MAIN HALL</h3>
  <p>A 127 square metre main hall with entrance lobby, toilets, a well-equipped kitchen and separate storage facilities. Three sets of double doors provide access to a large paved area and the adjacent playing field.</p>
  <div class="label">HALL CAPACITY:</div>
  <div class="value">180 PEOPLE</div>
  <div class="label">PRICE:</div>
  <div class="value">£10-20 PER HOUR</div>
  <div class="btns"><a class="btn b-white">More info</a><a class="btn b-orange">Book now</a></div>
</div>
<div class="abs fac fac-right">
  <h3>LARGE MEETING ROOM</h3>
  <p>A delightful, spacious room with an outlook and access to the small walled garden. Ideal for meetings and small gatherings - it has its own access door and the use of a disabled W/C. We offer a reduced rate for this room when booked together with the main hall.</p>
  <div class="label">HALL CAPACITY:</div>
  <div class="value">20 PEOPLE</div>
  <div class="label">PRICE:</div>
  <div class="value">£6-12 PER HOUR</div>
  <div class="btns"><a class="btn b-white">More info</a><a class="btn b-black">Book now</a></div>
</div>

<!-- where to go next -->
<h2 class="abs sec-title" style="top:2118px">Where to go next</h2>
<svg class="abs divider" style="top:2176px" viewBox="0 0 280 16"><line x1="0" y1="8" x2="280" y2="8" stroke="#333"/><rect x="110" y="2" width="60" height="12" rx="6" fill="#fff" stroke="#333"/></svg>
<div class="abs calendar">
  <div class="cal-month">February</div>
  <div class="cal-year">2021</div>
  <div class="cal-grid">
    <span class="hd sun">Sun</span><span class="hd">Mon</span><span class="hd">Tue</span><span class="hd">Wed</span><span class="hd">Thu</span><span class="hd">Fri</span><span class="hd">Sat</span>
    <span class="sunc"></span><span>1</span><span>2</span><span>3</span><span>4</span><span>5</span><span>6</span>
    <span class="sunc">7</span><span>8</span><span>9</span><span class="mark">10</span><span>11</span><span>12</span><span>13</span>
    <span class="sunc">14</span><span>15</span><span>16</span><span>17</span><span class="mark">18</span><span>19</span><span>20</span>
    <span class="sunc">21</span><span>22</span><span class="mark">23</span><span>24</span><span>25</span><span>26</span><span>27</span>
    <span class="sunc">28</span>
  </div>
</div>
<h3 class="abs free-title">CHECK WHEN THE HALL IS FREE</h3>
<div class="abs days"><span>10</span><span>18</span><span>23</span></div>
<p class="abs free-text">Lorem ipsum dolor sit amet, consectetur adipiscing elit, sed do eiusmod tempor incididunt Lorem ipsum dolor sit amet, consectetur adipiscing elit, sed do eiusmod</p>
<a class="abs btn policy">Read our booking policy</a>

<!-- amenities -->
<div class="abs amen" role="img" aria-label="Busy hall event with orange overlay"></div>
<h2 class="abs sec-title amen-title">Amenities</h2>
<svg class="abs divider" style="top:2744px" viewBox="0 0 280 16"><line x1="0" y1="8" x2="280" y2="8" stroke="#fff"/><rect x="110" y="2" width="60" height="12" rx="6" fill="#ee5a24" stroke="#fff"/></svg>
<div class="abs amen-item" style="left:113px"><div class="circle"><svg width="48" height="40" viewBox="0 0 48 40" fill="none" stroke="#ee5a24" stroke-width="3.5" stroke-linecap="round"><path d="M4 14a28 28 0 0 1 40 0"/><path d="M11 21a18 18 0 0 1 26 0"/><path d="M18 28a8 8 0 0 1 12 0"/><circle cx="24" cy="34" r="2" fill="#ee5a24"/></svg></div>Free WiFi</div>
<div class="abs amen-item" style="left:357px"><div class="circle"><svg width="52" height="36" viewBox="0 0 52 36" fill="none" stroke="#ee5a24" stroke-width="2.2"><path d="M6 24l4-10h22l5 10z"/><rect x="3" y="24" width="37" height="7" rx="2"/><circle cx="11" cy="32" r="3"/><circle cx="32" cy="32" r="3"/><rect x="38" y="2" width="12" height="12" rx="2"/><text x="41" y="12" font-size="10" fill="#ee5a24" stroke="none" font-family="Roboto" font-weight="700">P</text></svg></div>Free car parking</div>
<div class="abs amen-item" style="left:601px"><div class="circle"><svg width="46" height="42" viewBox="0 0 46 42" fill="none" stroke="#ee5a24" stroke-width="2.2"><rect x="4" y="12" width="38" height="28" rx="2"/><line x1="4" y1="20" x2="42" y2="20"/><rect x="10" y="25" width="14" height="10"/><circle cx="33" cy="29" r="4"/><path d="M12 4v6M20 4v6M28 4v6"/></svg></div>Fully equipped kitchen</div>
<div class="abs amen-item" style="left:845px"><div class="circle"><svg width="36" height="46" viewBox="0 0 36 46" fill="none" stroke="#ee5a24" stroke-width="2.4" stroke-linecap="round"><path d="M8 18a12 12 0 0 1 24 0c0 8-8 10-8 17a6 6 0 0 1-12 0"/><path d="M14 18a6 6 0 0 1 12 0c0 4-4 5-4 8"/></svg></div>Hearing loop</div>

<!-- upcoming events -->
<h2 class="abs sec-title" style="top:3055px">Upcoming activities and events</h2>
<svg class="abs divider" style="top:3114px" viewBox="0 0 280 16"><line x1="0" y1="8" x2="280" y2="8" stroke="#333"/><rect x="110" y="2" width="60" height="12" rx="6" fill="#fff" stroke="#333"/></svg>
<div class="abs event" style="left:111px">
  <div class="img" style="background:linear-gradient(180deg,#dcd8d0,#b9b2a4 55%,#efece6)" role="img" aria-label="Hall set for a dinner with round tables and chandelier"></div>
  <div class="date"><b>FEB</b><strong>10</strong></div>
  <h4>LOREM IPSUM DOLOR SIT AMET, CONSECTETUR ADIPISCING ELIT, SED DO</h4>
</div>
<div class="abs event" style="left:617px">
  <div class="img" style="background:linear-gradient(160deg,#3b1f63,#7a3fb0 45%,#c07a3a 80%,#4b2570)" role="img" aria-label="Lantern centrepiece on a table under purple lighting"></div>
  <div class="date"><b>FEB</b><strong>18</strong></div>
  <h4>LOREM IPSUM DOLOR SIT AMET, CONSECTETUR ADIPISCING ELIT, SED DO</h4>
</div>

<!-- news -->
<h2 class="abs sec-title" style="top:3596px">Our latest news</h2>
<svg class="abs divider" style="top:3654px" viewBox="0 0 280 16"><line x1="0" y1="8" x2="280" y2="8" stroke="#333"/><rect x="110" y="2" width="60" height="12" rx="6" fill="#fff" stroke="#333"/></svg>
<div class="abs news" style="left:111px">
  <div class="img" style="background:linear-gradient(180deg,#e8e9ee,#9aa6c2 55%,#2d3f7a)" role="img" aria-label="Hall with tables and blue chairs"></div>
  <h4>LOREM IPSUM DOLOR SIT AMET, CONSECTETUR</h4>
  <div class="date"><svg width="12" height="12" viewBox="0 0 12 12"><rect x="1" y="2" width="10" height="9" fill="#ee5a24"/></svg>Mar 20, 2020</div>
  <p>Lorem ipsum dolor sit amet, consectetur adipiscing elit, sed do eiusmod</p>
</div>
<div class="abs news" style="left:444px">
  <div class="img" style="background:linear-gradient(160deg,#1f3468,#c2612f 45%,#2c4a8a 80%,#c8bfb2)" role="img" aria-label="Stained glass windows in the hall"></div>
  <h4>LOREM IPSUM DOLOR SIT AMET, CONSECTETUR</h4>
  <div class="date"><svg width="12" height="12" viewBox="0 0 12 12"><rect x="1" y="2" width="10" height="9" fill="#ee5a24"/></svg>Mar 20, 2020</div>
  <p>Lorem ipsum dolor sit amet, consectetur adipiscing elit, sed do eiusmod</p>
</div>
<div class="abs news" style="left:777px">
  <div class="img" style="background:linear-gradient(180deg,#7fa7d8,#2f5a2a 45%,#8a3b2a 70%,#4d6b3a)" role="img" aria-label="Red brick hall building among trees"></div>
  <h4>LOREM IPSUM DOLOR SIT AMET, CONSECTETUR</h4>
  <div class="date"><svg width="12" height="12" viewBox="0 0 12 12"><rect x="1" y="2" width="10" height="9" fill="#ee5a24"/></svg>Mar 20, 2020</div>
  <p>Lorem ipsum dolor sit amet, consectetur adipiscing elit, sed do eiusmod</p>
</div>

<!-- footer -->
<footer class="abs footer"></footer>
<h3 class="abs f-title" style="left:115px;top:4280px;color:#fff">GET IN TOUCH</h3>
<p class="abs f-sub" style="left:117px;top:4326px">I offer online coaching and training plans for men and women.</p>
<div class="abs field" style="left:120px;top:4365px">Name</div>
<div class="abs field" style="left:356px;top:4365px">E - Mail</div>
<div class="abs field" style="left:120px;top:4424px">Subject</div>
<div class="abs field" style="left:356px;top:4424px">Message</div>
<div class="abs submit" style="color:#fff">SUBMIT</div>

<div class="abs contact" style="color:#fff">
  <h4 class="f-title" style="font-size:19px">CONTACT US</h4>
  <div class="c-row" style="margin-top:22px"><svg width="14" height="18" viewBox="0 0 14 18" fill="none" stroke="#fff" stroke-width="1.4"><path d="M7 17s6-6 6-10A6 6 0 0 0 1 7c0 4 6 10 6 10z"/><circle cx="7" cy="7" r="2"/></svg><span>123,Lorem ipsum dolor sit amet, consectetur adipiscing</span></div>
  <div class="c-row" style="margin-top:26px"><svg width="16" height="16" viewBox="0 0 16 16" fill="none" stroke="#fff" stroke-width="1.4"><path d="M3 1l3 3-2 2c1 2 4 5 6 6l2-2 3 3-2 2C7 15 1 9 1 3z"/></svg><span>Phone: +1 555 014 2290</span></div>
  <div class="c-row" style="margin-top:12px"><svg width="16" height="16" viewBox="0 0 16 16" fill="none" stroke="#fff" stroke-width="1.4"><rect x="1" y="6" width="14" height="8"/><rect x="4" y="1" width="8" height="5"/></svg><span>Fax:0330 555 0147</span></div>
  <div class="c-row" style="margin-top:12px"><svg width="16" height="14" viewBox="0 0 16 14" fill="none" stroke="#fff" stroke-width="1.4"><rect x="1" y="2" width="14" height="10"/><path d="M1 2l7 6 7-6"/></svg><span>Email: info@marlowickhall.org</span></div>
</div>
<div class="abs links" style="color:#fff">
  <h4 class="f-title" style="font-size:19px">QUICK LINKS</h4>
  <ul><li>Home</li><li>Calendar</li><li>Facilities</li><li>Prices</li><li>Photo</li><li>News</li><li>Contact Us</li></ul>
</div>
<div class="abs" style="left:0;top:4570px;width:1200px;height:1px;background:#222"></div>
<div class="abs bottom" style="left:109px">Login | Register | Privacy policy | Terms &amp; conditions</div>
<div class="abs social"><span>Chatterleaf</span><span>Quillcast</span></div>
<div class="abs bottom" style="left:774px">(c) 2021 Marlowick Hall | All Rights Reserved</div>

</body>
</html>
```